New website

We ned to create a new website that reflects more who we are. We are delivering exclusive premium products to our customers and the current website does not reflect our products at all.
We believe in less is more and need a webpage that is clean yet professional and exclusive.

Target Market(s)

Dentistry

Industry/Entity Type

Dental

Number of Pages Required

5+ page

Font styles to use
Sans Serif

Colors

Designer to choose colors to be used in the design.

Requirements
Must have
• Picture gallery
• Nice structure
• Clean layout
Nice to have
• Light fonts
Should not have
• Any italic font styles

```html
<!DOCTYPE html>
<html lang="en">
<head>
<meta charset="utf-8">
<title>Halvik Dental – Home</title>
<link href="https://fonts.googleapis.com/css2?family=Lato:wght@300;400;700&family=Montserrat:wght@400;600;700&display=swap" rel="stylesheet">
<style>
:root{
  --blue:#0d5ca8;
  --blue-dark:#0a4a8a;
  --red:#e31837;
  --ink:#262626;
  --text:#3a3a3a;
  --muted:#777;
  --light:#ececec;
  --line:#d9d9d9;
  --footer:#232323;
  --white:#fff;
}
*{box-sizing:border-box;margin:0;padding:0}
html,body{width:1200px;height:3888px;overflow:hidden}
body{font-family:'Lato',sans-serif;color:var(--text);background:var(--white);position:relative}
section,header,footer{position:absolute;left:0;width:1200px}
.heading{font-family:'Montserrat',sans-serif;font-weight:700;font-size:34px;text-align:center;letter-spacing:.5px}
.heading .red{color:var(--red)}
.heading .blue{color:var(--blue)}
.divider{display:block;margin:12px auto 0;width:30px;height:12px}
.divider span{display:inline-block;width:13px;height:12px;background:#9a9a9a}
.divider span+span{margin-left:4px;background:#c7c7c7}
.btn{display:inline-block;font-family:'Montserrat',sans-serif;font-weight:700;font-size:14px;color:var(--white);text-transform:uppercase;padding:12px 24px;border-radius:3px}
.btn-red{background:var(--red)}
.btn-blue{background:var(--blue)}

/* header */
.site-header{top:0;height:130px;background:var(--white);border-bottom:1px solid #eee}
.topbar{position:absolute;right:0;top:0;height:34px;display:flex;align-items:center}
.lang{font-size:13px;color:var(--ink);margin-right:20px;display:flex;align-items:center;gap:8px}
.lang i{display:inline-block;width:20px;height:12px;background:linear-gradient(#1d3f8f,#c8102e)}
.phone-tab{background:var(--red);color:var(--white);height:34px;display:flex;align-items:center;gap:10px;padding:0 20px 0 32px;font-family:'Montserrat',sans-serif;font-weight:700;font-size:17px;clip-path:polygon(16px 0,100% 0,100% 100%,0 100%)}
.phone-tab .ico{width:20px;height:20px;border-radius:50%;background:var(--white);display:flex;align-items:center;justify-content:center}
.socials{display:flex;gap:6px;background:var(--blue);height:34px;align-items:center;padding:0 16px}
.socials span{width:22px;height:22px;border-radius:50%;background:var(--white);opacity:.9}
.brand{position:absolute;left:98px;top:58px;display:flex;align-items:center;gap:12px}
.brand-dot{width:22px;height:22px;border-radius:50%;background:var(--blue)}
.brand-name{font-family:'Lato',sans-serif;font-weight:400;font-size:30px;color:var(--ink)}
.main-nav{position:absolute;left:430px;top:76px;display:flex}
.main-nav a{font-family:'Lato',sans-serif;font-size:14px;color:#555;text-decoration:none;text-transform:uppercase;padding:0 22px;border-right:1px solid var(--line);line-height:20px}
.main-nav a:last-child{border-right:0}
.main-nav a.active{color:var(--blue);font-weight:700}

/* hero */
.hero{top:130px;height:552px}
.hero-photo{position:absolute;inset:0;background:linear-gradient(100deg,#c9d4dc 0%,#e7ecef 35%,#b8c6cf 60%,#dfe6ea 100%)}
.hero-caption{position:absolute;left:0;top:202px;width:492px;height:160px;background:rgba(120,130,140,.55);color:var(--white);padding:24px 0 0 118px}
.hero-caption h1{font-family:'Montserrat',sans-serif;font-weight:600;font-size:28px;line-height:38px;letter-spacing:.5px}
.hero-caption p{font-size:14px;margin-top:8px;font-weight:700}
.hero-dots{position:absolute;left:248px;top:338px;display:flex;gap:5px}
.hero-dots span{width:12px;height:12px;border-radius:50%;background:var(--blue);border:2px solid var(--white)}
.hero-dots span:first-child{background:var(--red)}

/* about */
.about{top:682px;height:391px;text-align:center}
.about .heading{margin-top:50px}
.about p{width:1010px;margin:22px auto 0;font-size:14.5px;line-height:30px;color:var(--text)}
.about p strong{font-weight:700;color:var(--ink)}

/* feature panels */
.features{top:1073px;height:355px;display:flex}
.feature{width:600px;height:355px;padding:44px 0 0 98px;color:var(--white);position:relative}
.feature-blue{background:var(--blue)}
.feature-red{background:var(--red);padding-left:36px}
.feature h2{font-family:'Montserrat',sans-serif;font-weight:700;font-size:29px;display:flex;align-items:center;gap:16px;white-space:nowrap}
.feature-body{display:flex;gap:34px;margin-top:34px}
.feature-img{width:210px;height:180px;flex:none}
.feature-blue .feature-img{background:linear-gradient(#f4f6f8,#d8e2ea)}
.feature-red .feature-img{background:linear-gradient(#ffffff,#e6e6e6)}
.feature-text{width:250px;font-size:14px;line-height:23px;font-weight:700}
.feature .btn{margin-top:18px;padding:10px 22px}

/* services */
.services{top:1428px;height:659px;text-align:center}
.services .heading{margin-top:44px}
.services .intro{width:1020px;margin:24px auto 0;font-size:14.5px;line-height:30px}
.service-box{position:absolute;left:98px;top:296px;width:1004px;height:298px;border:1px solid var(--line)}
.service-icons{position:absolute;left:286px;top:252px;display:flex;gap:27px}
.service-icons span{width:88px;height:88px;border-radius:50%;background:var(--white);border:1px solid var(--line);display:flex;align-items:center;justify-content:center}
.service-icons span.active{background:var(--blue);border-color:var(--blue)}
.service-box h3{font-family:'Montserrat',sans-serif;font-weight:700;font-size:20px;color:var(--ink);margin-top:82px}
.service-box p{width:880px;margin:22px auto 0;font-size:14.5px;line-height:30px}

/* cta band */
.cta{top:2087px;height:155px;background:var(--light);display:flex;align-items:center;justify-content:center;gap:50px}
.cta p{font-family:'Montserrat',sans-serif;font-weight:600;font-size:30px;color:var(--ink)}
.cta .btn{font-size:16px;padding:14px 26px}

/* team */
.team{top:2242px;height:480px;background:linear-gradient(90deg,#eef1f3,#f8f9fa 45%,#e9edf0)}
.team .heading{margin-top:44px}
.team-cards{position:absolute;left:98px;top:155px;display:flex;gap:42px}
.member{width:485px;height:268px;background:var(--white);display:flex;box-shadow:0 1px 3px rgba(0,0,0,.08)}
.member-info{width:243px;padding:20px 18px 0 24px}
.member-info h4{font-size:18px;font-weight:400;color:var(--blue)}
.member-info .role{font-size:13px;color:var(--muted);margin-top:6px;padding-bottom:14px;border-bottom:1px solid var(--line)}
.member-info p{font-size:13px;line-height:23px;margin-top:14px;color:var(--text)}
.member-photo{flex:1;background:linear-gradient(#f2f4f6,#d9e1e7)}
.arrow{position:absolute;top:310px}

/* gallery */
.gallery{top:2722px;height:383px;text-align:center}
.gallery .heading{margin-top:50px}
.gallery-row{position:absolute;top:148px;left:0;width:1200px}
.pic{position:absolute;top:0;width:233px;height:155px;border:2px solid #5a4a48;border-radius:8px;background:radial-gradient(ellipse at center,#e9d7cf 0%,#b06862 45%,#6b2c2a 100%)}
.pic-label{position:absolute;top:172px;width:233px;font-family:'Montserrat',sans-serif;font-weight:600;font-size:14px;color:var(--ink)}
.swap-arrow{position:absolute;top:165px}

/* contact */
.contact{top:3105px;height:459px;background:var(--light)}
.map{position:absolute;left:98px;top:50px;width:472px;height:336px;background:linear-gradient(135deg,#e8ead8,#f3f1e6 50%,#dde6d0)}
.contact-form{position:absolute;left:625px;top:50px;width:477px}
.contact-form .heading{text-align:left;font-size:32px}
.contact-form .divider{margin:12px 0 0}
.fields{display:grid;grid-template-columns:1fr 1fr;gap:18px 14px;margin-top:26px}
.field{height:40px;background:var(--white);border:1px solid var(--line);font-size:12px;color:#999;padding:12px 14px}
.field.wide{grid-column:1/3;height:84px}
.contact-form .btn{margin-top:20px;padding:10px 30px}

/* footer */
.site-footer{top:3564px;height:324px;background:var(--footer);color:var(--white);overflow:hidden}
.footer-panel{position:absolute;right:0;top:0;width:422px;height:277px;background:var(--blue);clip-path:polygon(0 0,100% 0,100% 100%,70px 100%)}
.footer-col{position:absolute;top:40px}
.footer-col h5{font-family:'Montserrat',sans-serif;font-weight:700;font-size:14px;text-transform:uppercase;letter-spacing:.5px}
.footer-col ul{list-style:none;margin-top:18px}
.footer-col li{font-size:12.5px;line-height:28px;display:flex;align-items:flex-start;gap:10px}
.footer-col li svg{margin-top:8px;flex:none}
.footer-col li b{font-weight:700}
.links li::before{content:"›";color:#aaa}
.newsletter p{font-size:12px;line-height:16px;width:130px;margin:40px 0 0 2px;color:#ddd}
.subscribe{display:flex;margin-top:22px}
.subscribe span{width:160px;height:30px;background:var(--white);color:#999;font-size:11px;padding:8px 10px}
.subscribe b{width:76px;height:30px;background:var(--blue);font-size:11px;display:flex;align-items:center;justify-content:center}
.footer-brand{position:absolute;right:56px;top:104px;display:flex;flex-direction:column;align-items:center;gap:14px}
.footer-brand .brand-name{color:var(--white);font-size:26px}
.footer-brand .dots{display:flex;gap:6px}
.footer-brand .dots span{width:22px;height:22px;border-radius:50%;background:var(--white)}
.copyright{position:absolute;left:0;bottom:0;width:1200px;height:47px;background:#1a1a1a;text-align:center;font-size:12px;line-height:47px;color:#bbb}
.copyright b{color:var(--white)}
.to-top{position:absolute;right:100px;bottom:0;width:60px;height:47px;background:#333}
</style>
</head>
<body>

<header class="site-header">
  <div class="topbar">
    <div class="lang"><i></i>English ▾</div>
    <div class="phone-tab"><span class="ico"><svg width="12" height="12" viewBox="0 0 24 24"><path fill="#e31837" d="M6.6 10.8a15 15 0 006.6 6.6l2.2-2.2a1 1 0 011-.25 11.4 11.4 0 003.6.57 1 1 0 011 1V20a1 1 0 01-1 1A17 17 0 013 4a1 1 0 011-1h3.5a1 1 0 011 1c0 1.25.2 2.45.57 3.57a1 1 0 01-.25 1z"/></svg></span>040-12 34 56</div>
    <div class="socials"><span></span><span></span><span></span></div>
  </div>
  <div class="brand"><span class="brand-dot"></span><span class="brand-name">Halvik Dental</span></div>
  <nav class="main-nav">
    <a class="active">Home</a><a>About us ▾</a><a>Services ▾</a><a>Products ▾</a><a>Gallery</a><a>Contact us</a>
  </nav>
</header>

<section class="hero">
  <div class="hero-photo" role="img" aria-label="Smiling family of four on a bright beach"></div>
  <div class="hero-caption">
    <h1>HALVIK DENTAL &amp;<br>WINNING PRECISION</h1>
    <p>Lorem ipsum dolor sit amet, consectk etuer adipiscing</p>
  </div>
  <div class="hero-dots"><span></span><span></span><span></span><span></span><span></span></div>
</section>

<section class="about">
  <h2 class="heading"><span class="red">ABOUT</span> <span class="blue">US</span></h2>
  <div class="divider"><span></span><span></span></div>
  <p>Halvik Dental has met its customers since 1998. With the above all-ceramic constructions, we produce crown and bridge prosthetics of the highest quality. The specialty of cosmetic dentistry is where we are educated and have routines and predictable systems in the area. Halvik Dental's goal is to produce högkvalitiva products with the help of carefully selected products, equipment and the best technology. With this in mind, we can create a product of high quality, high aesthetics, fit and functionality. This is important because you do not have to use your work to a lot of unnecessary adjustments to the chair, but rather be cementing directly.<br><strong>With the patient in the first mind you will always be able to feel satisfied with our work ...</strong><br><strong>Halvik Dental, of course, quality assured to ISO 9000 and comply with the National Board requirements regarding medical devices.</strong></p>
</section>

<section class="features">
  <div class="feature feature-blue">
    <h2><svg width="46" height="34" viewBox="0 0 46 34"><circle cx="15" cy="9" r="7" fill="#fff"/><path d="M2 33c0-9 6-14 13-14s13 5 13 14z" fill="#fff"/><circle cx="32" cy="11" r="6" fill="#fff" opacity=".8"/><path d="M26 21c2-2 4-3 6-3 7 0 12 5 12 13H30z" fill="#fff" opacity=".8"/></svg>WHO WE ARE</h2>
    <div class="feature-body">
      <div class="feature-img" role="img" aria-label="Team of dentists in white coats"></div>
      <div class="feature-text">Lorem ipsum dolor sit amet, consectk etuer adipiscing elit, sed diam nonum my nibh euismod tinciduntut ut laoreet dolore magna aliquam erat volutpt. Ut wisi minim consequat.<br><span class="btn btn-red">Read more</span></div>
    </div>
  </div>
  <div class="feature feature-red">
    <h2><svg width="34" height="40" viewBox="0 0 34 40"><circle cx="17" cy="15" r="13" fill="#fff"/><path d="M9 25l-4 13 6-3 4 5 2-13zM25 25l4 13-6-3-4 5-2-13z" fill="#fff"/><path d="M11 15l4 4 8-8" stroke="#e31837" stroke-width="3" fill="none"/></svg>HALVIK DENTAL APP</h2>
    <div class="feature-body">
      <div class="feature-img" role="img" aria-label="Smartphone showing the clinic app"></div>
      <div class="feature-text">Halvik Dental has developed a phone app for anyone who is curious to know more about our products in general and the Halvik method in particular - and not least how...<br><span class="btn btn-blue">Read more</span></div>
    </div>
  </div>
</section>

<section class="services">
  <h2 class="heading"><span class="red">OUR</span> <span class="blue">SERVICES</span></h2>
  <div class="divider"><span></span><span></span></div>
  <p class="intro">While Halvik Dental provides extraordinary restorations, individual customer service and technical information, so we can advantageous offer our customers additional services. In these we find broad knowledge of different materials, techniques and design. We would like you to leave feedback if you think we are missing something, that facilitate your work is for the benefit of your patients. Click on the links below to learn more.</p>
  <div class="service-box">
    <h3>THE DIGITAL LAB</h3>
    <p>Now that all digitized its practitioners, this can be used also for communication purposes with us. With the help of digital cameras and digital X-ray, you can consult us about treatment therapies, preparations transmit information about color selection, etc. Either via DentShare, ScanLink Connect, email, C-rate link or memory card, data can be transferred directly to the lab. Color Capture and instructions no longer need to be written on the work order but sent down digitally. Do you have more ideas on how we can try to improve your life in practice - please send them to us.... [+]</p>
  </div>
  <div class="service-icons">
    <span class="active"><svg width="40" height="40" viewBox="0 0 40 40"><rect x="8" y="6" width="24" height="28" rx="10" fill="none" stroke="#fff" stroke-width="3"/><rect x="14" y="14" width="12" height="10" fill="#fff"/></svg></span>
    <span><svg width="40" height="40" viewBox="0 0 40 40"><path d="M8 8l6 16h16l2 8M14 24l-2 10M20 24h8" stroke="#333" stroke-width="3" fill="none"/><circle cx="12" cy="7" r="3" fill="#333"/></svg></span>
    <span><svg width="40" height="40" viewBox="0 0 40 40"><path d="M12 6c-5 0-6 6-5 10 1 5 3 8 4 18 1 2 3 2 4 0l2-10h6l2 10c1 2 3 2 4 0 1-10 3-13 4-18 1-4 0-10-5-10-3 0-5 2-8 2s-5-2-8-2z" fill="none" stroke="#333" stroke-width="2.5"/></svg></span>
    <span><svg width="40" height="40" viewBox="0 0 40 40"><rect x="4" y="12" width="32" height="16" rx="7" fill="none" stroke="#333" stroke-width="2.5"/><path d="M12 12v16M20 12v16M28 12v16" stroke="#333" stroke-width="2"/></svg></span>
    <span><svg width="40" height="40" viewBox="0 0 40 40"><path d="M6 30h28M10 30l4-12h14l4 12M18 18V8h8" stroke="#333" stroke-width="2.5" fill="none"/></svg></span>
  </div>
</section>

<section class="cta">
  <p>Lorem Ipsum is simply dummy text of theed.</p>
  <span class="btn btn-red">View our products</span>
</section>

<section class="team">
  <h2 class="heading"><span class="red">THE</span> <span class="blue">TEAM</span></h2>
  <div class="divider"><span></span><span></span></div>
  <div class="team-cards">
    <article class="member">
      <div class="member-info"><h4>Lina</h4><div class="role">Sed diam nonummy nibh euism</div><p>Lorem ipsum dolor sit amet, consectetuer adipiscing elit, sed diam nonummy nibh euismod tincidunt ut laoreet dolore magna aliquam erat volutpat. Ut wisi enim ad minim veniam, quis nostrud</p></div>
      <div class="member-photo" role="img" aria-label="Senior dentist holding a clipboard"></div>
    </article>
    <article class="member">
      <div class="member-info"><h4>Maja</h4><div class="role">Sed diam nonummy nibh euism</div><p>Lorem ipsum dolor sit amet, consectetuer adipiscing elit, sed diam nonummy nibh euismod tincidunt ut laoreet dolore magna aliquam erat volutpat. Ut wisi enim ad minim veniam, quis nostrud</p></div>
      <div class="member-photo" role="img" aria-label="Dentist with a stethoscope"></div>
    </article>
  </div>
  <svg class="arrow" style="left:38px" width="20" height="40" viewBox="0 0 20 40"><path d="M16 4L4 20l12 16" stroke="#777" stroke-width="2" fill="none"/></svg>
  <svg class="arrow" style="right:38px" width="20" height="40" viewBox="0 0 20 40"><path d="M4 4l12 16L4 36" stroke="#777" stroke-width="2" fill="none"/></svg>
</section>

<section class="gallery">
  <h2 class="heading"><span class="red">PHOTO</span> <span class="blue">GALLERY</span></h2>
  <div class="divider"><span></span><span></span></div>
  <div class="gallery-row">
    <div class="pic" style="left:98px" role="img" aria-label="Smile before treatment"></div>
    <div class="pic" style="left:347px" role="img" aria-label="Smile after treatment"></div>
    <div class="pic" style="left:625px" role="img" aria-label="Smile before treatment"></div>
    <div class="pic" style="left:871px" role="img" aria-label="Smile after treatment"></div>
    <div class="pic-label" style="left:98px">Before</div>
    <div class="pic-label" style="left:347px">After</div>
    <div class="pic-label" style="left:625px">Before</div>
    <div class="pic-label" style="left:871px">After</div>
    <svg class="swap-arrow" style="left:312px" width="52" height="24" viewBox="0 0 52 24"><path d="M2 6q24 18 44 2" stroke="#333" stroke-width="2.5" fill="none"/><path d="M40 4l8 3-6 6" stroke="#333" stroke-width="2.5" fill="none"/></svg>
    <svg class="swap-arrow" style="left:836px" width="52" height="24" viewBox="0 0 52 24"><path d="M2 6q24 18 44 2" stroke="#333" stroke-width="2.5" fill="none"/><path d="M40 4l8 3-6 6" stroke="#333" stroke-width="2.5" fill="none"/></svg>
    <svg style="position:absolute;left:38px;top:62px" width="20" height="40" viewBox="0 0 20 40"><path d="M16 4L4 20l12 16" stroke="#777" stroke-width="2" fill="none"/></svg>
    <svg style="position:absolute;right:38px;top:62px" width="20" height="40" viewBox="0 0 20 40"><path d="M4 4l12 16L4 36" stroke="#777" stroke-width="2" fill="none"/></svg>
  </div>
</section>

<section class="contact">
  <div class="map" role="img" aria-label="Street map of the city with the clinic location pinned"></div>
  <div class="contact-form">
    <h2 class="heading"><span class="red">QUICK</span> <span class="blue">CONTACT</span></h2>
    <div class="divider"><span></span><span></span></div>
    <div class="fields">
      <div class="field">First Name</div><div class="field">Last Name</div>
      <div class="field">Address</div><div class="field">Telephone</div>
      <div class="field wide">Message</div>
    </div>
    <span class="btn btn-blue">Submit</span>
  </div>
</section>

<footer class="site-footer">
  <div class="footer-panel"></div>
  <div class="footer-col" style="left:100px">
    <h5>Contact address</h5>
    <ul>
      <li><svg width="12" height="16" viewBox="0 0 12 16"><path d="M6 0a6 6 0 016 6c0 4-6 10-6 10S0 10 0 6a6 6 0 016-6z" fill="#fff"/><circle cx="6" cy="6" r="2" fill="#232323"/></svg><span><b>HALVIK DENTAL</b><br><span style="line-height:16px;display:block">Halvik Dental AB<br>Box 10020 20000 Nordstad, Sweden</span></span></li>
      <li><svg width="12" height="12" viewBox="0 0 24 24"><path fill="#fff" d="M6.6 10.8a15 15 0 006.6 6.6l2.2-2.2a1 1 0 011-.25 11.4 11.4 0 003.6.57 1 1 0 011 1V20a1 1 0 01-1 1A17 17 0 013 4a1 1 0 011-1h3.5a1 1 0 011 1c0 1.25.2 2.45.57 3.57a1 1 0 01-.25 1z"/></svg>040-12 34 56</li>
      <li><svg width="12" height="12" viewBox="0 0 12 12"><rect x="1" y="2" width="10" height="8" fill="#fff"/></svg>123-000-4567</li>
      <li><svg width="12" height="12" viewBox="0 0 12 12"><rect x="0" y="2" width="12" height="8" fill="#fff"/><path d="M0 2l6 5 6-5" stroke="#232323" fill="none"/></svg>info@halvikdental.example</li>
    </ul>
  </div>
  <div class="footer-col links" style="left:372px">
    <h5>Quick links</h5>
    <ul><li>Home</li><li>About Us</li><li>Our Service</li><li>Products</li><li>Gallery</li><li>Contact Us</li></ul>
  </div>
  <div class="footer-col newsletter" style="left:545px">
    <h5>Newsletter signup</h5>
    <svg style="position:absolute;left:150px;top:36px" width="70" height="50" viewBox="0 0 70 50"><path d="M2 22L68 2 50 46 34 30z" fill="none" stroke="#888" stroke-width="2"/><path d="M34 30L68 2" stroke="#888" stroke-width="2"/></svg>
    <p>Get the latest news by entering your email address</p>
    <div class="subscribe"><span>Email Address</span><b>SUBSCRIBE</b></div>
  </div>
  <div class="footer-brand">
    <span class="brand-name">Halvik Dental</span>
    <div class="dots"><span></span><span></span><span></span></div>
  </div>
  <div class="copyright">© 2017 <b>Halvik Dental.</b> All Rights Reserved.</div>
  <div class="to-top"><svg style="margin:18px 0 0 22px" width="16" height="10" viewBox="0 0 16 10"><path d="M1 9l7-7 7 7" stroke="#fff" stroke-width="2" fill="none"/></svg></div>
</footer>

</body>
</html>
```